Silverfern Hollow Counseling business cards

Dana Porvette, LCPC, NCC
(555)347-0816
www.silverfernhollowcounseling.example
dana@silverfernhollowcounseling.example

Business cards. I would like it on the same background as pictured. Not on a white business card. I have attached the logo that was done by another designer with artmarketly. I am open to looking at single-sided and double-sided designs.

Target Market(s)

teenagers and adults

Industry/Entity Type

mental health

Contact Information for Business Card

Dana Porvette, LCPC, NCC (555)347-0816 dana@silverfernhollowcounseling.example

Font styles to use
Other font styles liked:
• Cinzel

Colors

Designer to choose colors to be used in the design.

Requirements
Must have
• logo that is attached

```html
<!DOCTYPE html>
<html lang="en">
<head>
<meta charset="UTF-8">
<title>Silverfern Hollow Counseling – Business Cards</title>
<link rel="stylesheet" href="https://fonts.googleapis.com/css2?family=Cinzel:wght@400;500&family=Lato:wght@400&family=Montserrat:wght@700&display=swap">
<style>
  :root {
    --stage: #1c1d1f;
    --card-front: #0c4668;
    --card-front-deep: #083a58;
    --card-back-top: #3d4a57;
    --card-back-bottom: #1c2733;
    --edge-teal: #3aa99f;
    --accent-coral: #e08a68;
    --name-teal: #4cb8ad;
    --brand-blue: #1d6fae;
    --text-light: #f2f5f7;
  }
  * { box-sizing: border-box; margin: 0; padding: 0; }
  html, body {
    width: 1200px; height: 800px; overflow: hidden;
    background: var(--stage);
  }
  .sheet {
    width: 1200px; height: 800px;
    display: flex; align-items: center; justify-content: center; gap: 40px;
  }
  .card {
    position: relative;
    width: 540px; height: 309px;
    border-radius: 22px;
    border-bottom: 4px solid var(--edge-teal);
    overflow: hidden;
    box-shadow: 0 18px 40px rgba(0,0,0,.55);
  }
  /* Contact side */
  .card--contact {
    background: linear-gradient(160deg, var(--card-front) 0%, var(--card-front-deep) 100%);
  }
  .brand-mark {
    position: absolute; top: 40px; right: 40px;
    display: flex; align-items: center; gap: 12px;
  }
  .brand-dot {
    width: 30px; height: 30px; border-radius: 50%;
    background: var(--edge-teal);
  }
  .brand-name {
    font-family: "Montserrat", sans-serif; font-weight: 700;
    color: var(--text-light);
    font-size: 15px; line-height: 1.25; letter-spacing: .5px;
    text-transform: uppercase; text-align: center;
  }
  .divider {
    position: absolute; left: 40px; right: 40px; top: 168px;
    height: 1px; background: var(--accent-coral);
  }
  .person-name {
    position: absolute; left: 40px; top: 128px;
    font-family: "Cinzel", serif; font-weight: 400;
    font-size: 25px; color: var(--name-teal); letter-spacing: 1px;
  }
  .contact-list {
    position: absolute; left: 40px; top: 188px;
    list-style: none;
    font-family: "Lato", sans-serif; font-size: 14px;
    color: var(--text-light);
  }
  .contact-list li {
    display: flex; align-items: center; gap: 10px;
    margin-bottom: 9px;
  }
  .contact-icon { width: 14px; height: 14px; flex: none; }
  /* Brand side */
  .card--brand {
    background: linear-gradient(170deg, var(--card-back-top) 0%, var(--card-back-bottom) 100%);
    display: flex; flex-direction: column; align-items: center; justify-content: center; gap: 20px;
  }
  .brand-dot--large { width: 64px; height: 64px; }
  .brand-name--large {
    font-size: 32px; line-height: 1.15; color: var(--brand-blue); letter-spacing: 1px;
  }
</style>
</head>
<body>
<main class="sheet">
  <section class="card card--contact">
    <div class="brand-mark">
      <span class="brand-dot"></span>
      <p class="brand-name">Silverfern Hollow<br>Counseling</p>
    </div>
    <h1 class="person-name">DANA PORVETTE, LCPC, NCC</h1>
    <div class="divider"></div>
    <ul class="contact-list">
      <li>
        <svg class="contact-icon" viewBox="0 0 24 24"><path fill="#4cb8ad" d="M6.6 10.8a15 15 0 0 0 6.6 6.6l2.2-2.2c.3-.3.7-.4 1-.2 1.1.4 2.3.6 3.6.6.6 0 1 .4 1 1V20c0 .6-.4 1-1 1C10.6 21 3 13.4 3 4c0-.6.4-1 1-1h3.5c.6 0 1 .4 1 1 0 1.3.2 2.5.6 3.6.1.3 0 .7-.2 1z"/></svg>
        (555)347-0816
      </li>
      <li>
        <svg class="contact-icon" viewBox="0 0 24 24"><path fill="#4cb8ad" d="M3 5h18v14H3z"/><path fill="none" stroke="#0c4668" stroke-width="2" d="M3 6l9 7 9-7"/></svg>
        dana@silverfernhollowcounseling.example
      </li>
      <li>
        <svg class="contact-icon" viewBox="0 0 24 24"><circle cx="12" cy="12" r="9" fill="none" stroke="#4cb8ad" stroke-width="2"/><path fill="none" stroke="#4cb8ad" stroke-width="2" d="M3 12h18M12 3c3 3 3 15 0 18M12 3c-3 3-3 15 0 18"/></svg>
        silverfernhollowcounseling.example
      </li>
    </ul>
  </section>

  <section class="card card--brand">
    <span class="brand-dot brand-dot--large"></span>
    <p class="brand-name brand-name--large">Silverfern Hollow<br>Counseling</p>
  </section>
</main>
</body>
</html>
```